Trap Meets Cosmic – Lunar Rancher Brand Redesign Packaging Brief

Lunar Rancher – Brand Revamp Creative Brief

Objective:
Revamp the Lunar Rancher brand into a cohesive, standout identity that can flex across multiple products and flavor SKUs. The look should feel like a movement—uniform enough to be recognizable at a glance, but wild enough to stand out in the category.

Core Identity:

Always Aesthetic – visually striking and memorable.

Uniform but Wild – one unified system with room for bold, unique flavor expressions.

Branded like a Movement – feels grassroots, organic, built by the culture.

Built Different – trappy, not corporate.

Culture Bred – tied to music, nightlife, and community energy.

Brand Voice & Tone:

Slang-friendly, slick, and authentic.

Confident, not corporate.

Feels like that one friend who always has snacks, the aux cord, and fire fits.

Flavor Lineup & Style Directions

1. Violet Nebula

Flavor: Grape + cotton candy

Look: Trippy, purple chrome label, space haze effects

2. Berry Ooze

Flavor: Black cherry

Look: Dark red metallic, syrupy drip motif

3. Dusk Papaya

Flavor: Mango Kush

Look: Dark gold + black cosmic background, luxury meets space

4. Orbit Agave

Flavor: Prickly pear

Look: Neon green palette with desert moon + alien cactus silhouette

5. Rose Comet

Flavor: Strawberry lemonade

Look: Pastel pink with radiant starburst

6. Gritzlefruit

Flavor: Apple + blueberry

Look: Trap camo motif in blue/green—gritty but vibrant

7. Bandit Tangelo

Flavor: Tangy citrus

Look: Orange sunset gradient, western-inspired font twist

8. Thruster Bloo

Flavor: Blue raspberry

Look: Electric blue rocket iconography, explosive energy

9. Diesel Plum

Flavor: Concord grape + fuel

Look: Dark purple base with chrome gas-can accents

10. Spicy Glow Jupiter

Flavor: Peach + chili

Look: Orange-red palette with Saturn ring orbit detail

11. Cream Abyss

Flavor: Vanilla + marshmallow

Look: Creamy white palette, black hole/singularity graphics

12. Oakbark Frost

Flavor: Cherry + menthol

Look: Smoky woodgrain textures, cold fog overlay

13. Quasar Lychee

Flavor: Guava + passionfruit

Look: Pink-orange gradient with abstract space glyphs

Designer Notes:

Create one master design system (logo lockup, typography, brand assets) that allows these flavors to live in the same world while each feeling distinct.

Prioritize a balance of trappy grit and cosmic surrealism. Think bold textures, metallic finishes, gradients, and chrome accents that feel late-night, music-driven, non-corporate.

Deliverables should work across packaging (jars, Mylar, disposables), merch, and digital/social assets.

Target Market(s)

Gen Z & Millennials Hip-hop/trap culture fans . Urban & creative subcultures (artists, sneakerheads, gamers)

Industry/Entity Type

Cannabis

Requirements
Must have
• Must use the logos included. One style and one feel but also be able to have different 13 flavors for 5 different types of infused products . We a highend finish. We want it to be colorful and have holographic finishes and everyhing to make it pop and stand out.
Nice to have
• different flavors and colors but all needs to be in the same style. Trap and aggressive looking
Should not have
• No weed leafs. not appealing to children.

```html
<!DOCTYPE html>
<html lang="en">
<head>
<meta charset="utf-8">
<title>Lunar Rancher – Berry Ooze Pouch</title>
<link rel="stylesheet" href="https://fonts.googleapis.com/css2?family=Luckiest+Guy&family=Oswald:wght@600&display=swap">
<style>
  :root {
    --backdrop: #c8c8c8;
    --swirl-violet: #7c82e0;
    --swirl-pink: #e08fcf;
    --swirl-teal: #7fcfc4;
    --swirl-gold: #e6b93a;
    --swirl-orange: #d98a3c;
    --ink: #17171b;
    --cherry-red: #e0262f;
    --cherry-deep: #9e0f18;
    --burst-white: #fbf7fb;
    --burst-edge: #c86fb8;
    --pill-white: #f4f4f4;
  }
  html, body {
    margin: 0;
    width: 1200px;
    height: 1200px;
    overflow: hidden;
    background: var(--backdrop);
  }
  .canvas {
    position: relative;
    width: 1200px;
    height: 1200px;
  }
  .pouch {
    position: absolute;
    left: 280px;
    top: 50px;
    width: 640px;
    height: 1100px;
    border-radius: 6px;
    overflow: hidden;
  }
  .pouch-art {
    position: absolute;
    inset: 0;
    background:
      radial-gradient(ellipse at 50% 55%, var(--swirl-pink) 0%, transparent 45%),
      radial-gradient(ellipse at 20% 20%, var(--swirl-gold) 0%, transparent 40%),
      radial-gradient(ellipse at 85% 30%, var(--swirl-teal) 0%, transparent 45%),
      radial-gradient(ellipse at 15% 80%, var(--swirl-orange) 0%, transparent 40%),
      radial-gradient(ellipse at 85% 85%, var(--swirl-gold) 0%, transparent 40%),
      var(--swirl-violet);
  }
  .zip-seal {
    position: absolute;
    left: 0;
    right: 0;
    top: 98px;
    height: 3px;
    background: rgba(255,255,255,0.25);
  }
  .brand-name {
    position: absolute;
    left: 40px;
    top: 218px;
    width: 410px;
    margin: 0;
    text-align: center;
    font-family: "Oswald", sans-serif;
    font-weight: 600;
    font-size: 54px;
    line-height: 1;
    text-transform: uppercase;
    color: var(--ink);
  }
  .burst {
    position: absolute;
    left: 20px;
    top: 410px;
    width: 580px;
    height: 360px;
  }
  .fruit-art {
    position: absolute;
    left: 178px;
    top: 362px;
    width: 132px;
    height: 132px;
    border-radius: 50%;
    background: radial-gradient(circle at 40% 35%, var(--cherry-red), var(--cherry-deep));
  }
  .flavor-title {
    position: absolute;
    left: 60px;
    top: 510px;
    width: 500px;
    margin: 0;
    text-align: center;
    font-family: "Luckiest Guy", cursive;
    font-size: 104px;
    line-height: 0.92;
    color: var(--cherry-red);
    -webkit-text-stroke: 3px var(--cherry-deep);
    letter-spacing: 1px;
  }
  .flavor-pill {
    position: absolute;
    left: 189px;
    top: 976px;
    width: 252px;
    height: 48px;
    border-radius: 24px;
    background: var(--pill-white);
    display: flex;
    align-items: center;
    justify-content: center;
    font-family: "Oswald", sans-serif;
    font-weight: 600;
    font-size: 26px;
    letter-spacing: 0.5px;
    color: var(--ink);
  }
</style>
</head>
<body>
  <main class="canvas">
    <section class="pouch">
      <div class="pouch-art" role="img" aria-label="Psychedelic liquid swirl pattern in violet, pink, teal, gold and orange radiating from the centre"></div>
      <div class="zip-seal"></div>

      <p class="brand-name">Lunar Rancher</p>

      <svg class="burst" viewBox="0 0 580 360" role="img" aria-label="Comic starburst with puffs of smoke and lightning bolts">
        <polygon fill="var(--burst-white)" stroke="var(--burst-edge)" stroke-width="8" stroke-linejoin="round"
          points="140,30 210,70 290,10 350,70 450,40 450,110 560,130 480,185 570,250 450,255 470,340 360,290 300,355 230,290 120,340 140,260 10,250 100,190 20,120 130,110"/>
      </svg>

      <div class="fruit-art" role="img" aria-label="Pair of glossy red cherries on stems"></div>

      <h1 class="flavor-title">Berry<br>Ooze</h1>

      <div class="flavor-pill">BLACK CHERRY</div>
    </section>
  </main>
</body>
</html>
```